Business Card - KIRBY Real Estate

Design a professional business card for a real estate agent.

Target Market(s)

Residential property and home owners in the middle suburban eastern suburbs of Melbourne, Australia. Property prices range between $1m and $3m in value.

Industry/Entity Type

Real Estate

Contact Information for Business Card

FRONT: Black on White
KIRBY Real Estate logo
Callum Kirby
Director / Officer in Effective Control / CEA TLGU
52 Marrow Street,
Ferncliff East VIC 3187
Tel: 1800 672 918
Mob: 0412 608 274
E: callum@kirbyrealestate.com.au
W. www.kirbyrealestate.com.au

BACK: White on Black logo
KIRBY Real Estate logo
website: www.kirbyrealestate.com.au

Colors
ffffff
000000

Requirements
Must have
• Detail as specified above
• White on black for front
• Black on white for back
Nice to have
• I may like to integrate my photo on the card;
• there will be other agents also requiring the card so a template would be useful
Should not have
• animations / drawings

```html
<!DOCTYPE html>
<html lang="en">
<head>
<meta charset="utf-8">
<title>KIRBY Real Estate – Business Card</title>
<link href="https://fonts.googleapis.com/css2?family=Questrial&display=swap" rel="stylesheet">
<style>
  :root {
    --stage: #6f7c91;
    --paper: #ffffff;
    --ink: #111111;
    --ink-soft: #333333;
    --black: #0c0c0c;
    --photo-light: #f4f4f4;
    --photo-mid: #d9d9d9;
    --reverse: #f2f2f2;
  }
  * { box-sizing: border-box; margin: 0; padding: 0; }
  html, body {
    width: 1200px; height: 810px; overflow: hidden;
    background: var(--stage);
    font-family: "Questrial", "Century Gothic", sans-serif;
  }
  .canvas {
    position: relative; width: 1200px; height: 810px;
    display: flex; align-items: center; justify-content: center; gap: 40px;
  }
  .card {
    position: relative; width: 520px; height: 297px; overflow: hidden;
    box-shadow: 0 6px 18px rgba(0,0,0,.25);
  }
  /* Front */
  .card-front { background: var(--paper); color: var(--ink); }
  .agent-photo {
    position: absolute; left: 0; top: 0; width: 230px; height: 100%;
    background: radial-gradient(ellipse at 50% 40%, var(--photo-light), var(--photo-mid));
  }
  .photo-base {
    position: absolute; left: 0; bottom: 0; width: 230px; height: 38px;
    background: var(--black);
  }
  .details {
    position: absolute; left: 256px; top: 30px; right: 22px;
  }
  .brand {
    font-size: 20px; letter-spacing: 1px; color: var(--ink); white-space: nowrap;
    margin-bottom: 20px; display: flex; align-items: center; gap: 8px;
  }
  .brand-dot { width: 10px; height: 10px; background: var(--ink); flex: none; }
  .agent-name { font-size: 20px; font-weight: 700; color: var(--ink); white-space: nowrap; }
  .agent-role { font-size: 12px; color: var(--ink-soft); margin-bottom: 12px; }
  .contact-row {
    display: flex; justify-content: space-between; align-items: flex-start; gap: 8px;
    font-size: 12px; line-height: 1.4; color: var(--ink-soft); margin-bottom: 8px;
    white-space: nowrap;
  }
  .contact-row svg { flex: none; width: 12px; height: 12px; margin-top: 2px; fill: var(--ink); }
  /* Back */
  .card-back {
    background: linear-gradient(135deg, #2a2a2a 0%, var(--black) 55%, #1b1b1b 100%);
    display: flex; align-items: center; justify-content: center;
  }
  .brand-reverse {
    font-size: 40px; letter-spacing: 4px; color: var(--reverse); white-space: nowrap;
  }
</style>
</head>
<body>
<main class="canvas">
  <section class="card card-front" aria-label="Business card front">
    <div class="agent-photo" role="img" aria-label="Portrait photo of the agent standing in a dark suit"></div>
    <div class="photo-base"></div>
    <div class="details">
      <div class="brand"><span class="brand-dot"></span>KIRBY Real Estate</div>
      <h1 class="agent-name">Callum Kirby</h1>
      <p class="agent-role">Director</p>
      <div class="contact-row">
        <span>52 Marrow Street,<br>Ferncliff East VIC 3187</span>
        <svg viewBox="0 0 12 12" aria-hidden="true"><path d="M6 0a4 4 0 0 0-4 4c0 3 4 8 4 8s4-5 4-8a4 4 0 0 0-4-4zm0 5.6A1.6 1.6 0 1 1 6 2.4a1.6 1.6 0 0 1 0 3.2z"/></svg>
      </div>
      <div class="contact-row">
        <span>1800 672 918<br>0412 608 274</span>
        <svg viewBox="0 0 12 12" aria-hidden="true"><path d="M2.5 0.5l2 2.2-1.1 1.4c.7 1.6 2 2.9 3.5 3.6l1.4-1.1 2.2 2-1.3 2.1C4.8 10.4 1.3 6.8.6 2z"/></svg>
      </div>
      <div class="contact-row">
        <span>callum@kirbyrealestate.com.au<br>www.kirbyrealestate.com.au</span>
        <svg viewBox="0 0 12 12" aria-hidden="true"><circle cx="6" cy="6" r="5.2" fill="none" stroke="#111" stroke-width="1.2"/><path d="M0.8 6h10.4M6 0.8c-2.6 3-2.6 7.4 0 10.4M6 0.8c2.6 3 2.6 7.4 0 10.4" fill="none" stroke="#111" stroke-width="1"/></svg>
      </div>
    </div>
  </section>
  <section class="card card-back" aria-label="Business card back">
    <div class="brand-reverse">KIRBY Real Estate</div>
  </section>
</main>
</body>
</html>
```